Need a webinar banner promo to place on social media

We are organise a series of webinars in coming months.

We need a webinar banner design to be posted on Facebook and linkedin. The banner is for our webinar titled: Steps to Unveil your venture with poise and polish.

our website is www.bravolinhub.com.au

there is a link on the website to the webinar registration for your reference.

```html
<!DOCTYPE html>
<html lang="en">
<head>
<meta charset="utf-8">
<title>Webinar Banner – Steps to Unveil Your Venture</title>
<link rel="stylesheet" href="https://fonts.googleapis.com/css2?family=Montserrat:wght@300;400;700;800&display=swap">
<style>
  :root {
    --navy: #14284b;
    --navy-deep: #1b3158;
    --slate: #3a4a52;
    --gold: #b08a2e;
    --gold-light: #e4d26c;
    --gold-mid: #c9b24e;
    --gold-dark: #9c8337;
    --photo-a: #2b2d38;
    --photo-b: #232a44;
    --white: #ffffff;
    --stage: #1c1c1c;
  }
  * { margin: 0; padding: 0; box-sizing: border-box; }
  html, body {
    width: 1200px; height: 703px; overflow: hidden;
    background: var(--stage);
    font-family: "Montserrat", sans-serif;
  }
  .banner {
    position: absolute; left: 0; top: 37px;
    width: 1200px; height: 628px;
    background: var(--white);
    overflow: hidden;
    color: var(--navy);
  }
  .brand {
    position: absolute; left: 52px; top: 92px;
    display: flex; align-items: center; gap: 12px;
  }
  .brand-square { width: 26px; height: 26px; background: var(--navy); }
  .brand-name {
    font-weight: 800; font-size: 32px; letter-spacing: -0.5px;
    color: var(--navy); line-height: 1;
  }
  .headline {
    position: absolute; left: 429px; top: 78px;
    font-size: 41px; line-height: 56px; letter-spacing: -0.5px;
    text-transform: uppercase; color: var(--navy); white-space: nowrap;
  }
  .headline .light { font-weight: 300; }
  .headline .bold { font-weight: 800; }
  .band { position: absolute; left: 0; top: 252px; width: 1200px; height: 291px; }
  .webinar-tab {
    position: absolute; left: 45px; top: 236px;
    width: 321px; height: 40px;
    background: var(--white); border-radius: 9px;
    display: flex; align-items: center; justify-content: center;
    font-weight: 800; font-size: 33px; color: var(--gold); letter-spacing: 0.5px;
  }
  .rule { position: absolute; left: 49px; width: 440px; height: 1.5px; background: var(--white); }
  .rule-top { top: 314px; }
  .rule-bottom { top: 454px; }
  .date-day {
    position: absolute; left: 44px; top: 316px;
    font-weight: 800; font-size: 152px; line-height: 1; letter-spacing: -8px;
    color: var(--navy);
  }
  .date-month, .date-year {
    position: absolute; left: 219px;
    font-weight: 800; font-size: 60px; line-height: 1; color: var(--navy);
  }
  .date-month { top: 326px; }
  .date-year { top: 389px; letter-spacing: -1px; }
  .time {
    position: absolute; left: 48px; top: 466px;
    font-weight: 800; font-size: 34px; color: var(--navy); letter-spacing: -0.3px;
  }
  .register {
    position: absolute; left: 49px; top: 562px; height: 38px;
    display: flex; align-items: center; gap: 16px;
  }
  .register-label { font-weight: 400; font-size: 25px; color: var(--navy); }
  .register-link {
    height: 38px; padding: 0 20px 0 12px;
    display: flex; align-items: center;
    background: linear-gradient(90deg, var(--gold-dark), var(--gold-mid) 55%, #d9bf55);
    border-radius: 0 19px 19px 0;
    font-weight: 800; font-size: 22px; color: var(--navy);
  }
  .speakers-photo {
    position: absolute; left: 650px; top: 216px;
    width: 530px; height: 412px;
    background: linear-gradient(135deg, var(--photo-a), var(--photo-b));
  }
</style>
</head>
<body>
  <main class="banner">
    <div class="brand">
      <span class="brand-square"></span>
      <span class="brand-name">LUMEN WRITERS</span>
    </div>

    <h1 class="headline">
      <span class="light">Steps to unveil</span> <span class="bold">your venture</span><br>
      <span class="bold">with poise and polish.</span>
    </h1>

    <svg class="band" viewBox="0 0 1200 291" preserveAspectRatio="none" aria-hidden="true">
      <defs>
        <linearGradient id="goldFill" x1="0" y1="0" x2="1" y2="0.4">
          <stop offset="0" stop-color="#e9d873"/>
          <stop offset="0.45" stop-color="#c9b24e"/>
          <stop offset="1" stop-color="#a38c3c"/>
        </linearGradient>
      </defs>
      <polygon points="0,0 620,0 580,291 0,291" fill="url(#goldFill)"/>
      <polygon points="620,0 636,0 599,291 580,291" fill="var(--slate)"/>
      <polygon points="636,0 1200,0 1200,291 599,291" fill="var(--navy-deep)"/>
    </svg>

    <div class="webinar-tab">FREE WEBINAR</div>
    <div class="rule rule-top"></div>
    <div class="date-day">15</div>
    <div class="date-month">MARCH</div>
    <div class="date-year">2023</div>
    <div class="rule rule-bottom"></div>
    <div class="time">7:00 PM – 8:00 PM AEDT</div>

    <div class="register">
      <span class="register-label">Register Now</span>
      <span class="register-link">www.bravolinhub.com.au</span>
    </div>

    <div class="speakers-photo" role="img" aria-label="Photo of two smiling hosts in formal suits, one holding a gold award trophy"></div>
  </main>
</body>
</html>
```